Business Card Design Project

I am looking for a business card design for my custom Audio/Video & Contracting business named Brelvora Systems Inc. We do not currently have a corporate logo so you should not feel constrained to work around an existing design. Your design should be elegant and clean while artistically conveying that we are a technology company. We provide A/V services for the commercial and residential markets and contracting services for residential remodeling and home theater construction. We do not have a particular color that we are looking to design around so feel free to be creative.

To get references of the kind of work that we do and design inspiration please visit the following sites:

http://www.quenlamark.us
www.morvethpro.com
www.feltonbraxa.com

Reason: I think we are getting close on a couple of the designs and want to give additional time to get tweaks done and to resubmit your designs.

Target Market(s)

Most of our clients are very wealthy and have been exposed to premium brand names in every aspect of their lives, (ie. - luxury autos, estate sized homes, fine jewelery and clothes) and your design needs to convey that same level of excellent design that they are used to.

Industry/Entity Type

Residential

Requirements
Should not have
• An extensive use of the color RED.

```html
<!DOCTYPE html>
<html lang="en">
<head>
<meta charset="utf-8">
<title>Brelvora Systems Inc. – Business Card</title>
<link rel="stylesheet" href="https://fonts.googleapis.com/css2?family=Questrial&display=swap">
<style>
  :root {
    --card-bg: #f0f0f0;
    --brand-blue: #1a7db5;
    --text-dark: #2e2e2e;
    --reel-blue: #c8d9e8;
    --strip-grey: #c4c4c4;
  }
  html, body {
    margin: 0;
    padding: 0;
    overflow: hidden;
    background: var(--card-bg);
  }
  .card {
    position: relative;
    width: 1200px;
    height: 686px;
    background: var(--card-bg);
    overflow: hidden;
    font-family: "Questrial", "Century Gothic", sans-serif;
  }
  .reel-art {
    position: absolute;
    left: 660px;
    top: 150px;
    width: 540px;
    height: 536px;
  }
  .wordmark {
    position: absolute;
    left: 120px;
    top: 280px;
    width: 445px;
    text-align: left;
    color: var(--brand-blue);
    font-weight: 400;
  }
  .wordmark-name {
    display: block;
    font-size: 74px;
    line-height: 80px;
    letter-spacing: 6px;
    text-transform: lowercase;
  }
  .wordmark-sub {
    display: block;
    margin-top: 8px;
    font-size: 31px;
    line-height: 36px;
    letter-spacing: 11.5px;
    text-transform: uppercase;
  }
  .divider {
    position: absolute;
    left: 599px;
    top: 171px;
    width: 2px;
    height: 343px;
    background: var(--brand-blue);
  }
  .contact {
    position: absolute;
    left: 654px;
    top: 0;
    margin: 0;
    padding: 0;
    list-style: none;
    color: var(--text-dark);
    font-size: 26px;
  }
  .contact-item {
    position: absolute;
    left: 0;
    white-space: nowrap;
    line-height: 30px;
  }
  .contact-name    { top: 182px; }
  .contact-address { top: 229px; }
  .contact-cell    { top: 325px; }
  .contact-email   { top: 372px; }
  .contact-website { top: 466px; }
</style>
</head>
<body>
  <div class="card">
    <svg class="reel-art" role="img" aria-label="Illustration of a pale blue film reel wrapped by a grey film strip, with small music notes and motion swooshes" viewBox="0 0 540 536" xmlns="http://www.w3.org/2000/svg">
      <defs>
        <radialGradient id="reelTone" cx="50%" cy="50%" r="50%">
          <stop offset="0%" stop-color="#dfe4e9"/>
          <stop offset="60%" stop-color="#cfdce8"/>
          <stop offset="100%" stop-color="#c8d9e8"/>
        </radialGradient>
      </defs>
      <circle cx="289" cy="273" r="217" fill="url(#reelTone)"/>
    </svg>

    <div class="wordmark">
      <span class="wordmark-name">brelvora</span>
      <span class="wordmark-sub">Systems Inc.</span>
    </div>

    <div class="divider"></div>

    <ul class="contact">
      <li class="contact-item contact-name">Name</li>
      <li class="contact-item contact-address">Address</li>
      <li class="contact-item contact-cell">Cell number</li>
      <li class="contact-item contact-email">Email address</li>
      <li class="contact-item contact-website">Website</li>
    </ul>
  </div>
</body>
</html>
```